Powerpoint template for Trivia Company

Revamp of our current powerpoint template to make it more professional and fun for the players. Something worthy of a trivia company. Please see logo attached for potential colour - but also open to other ideas.

NO BRANDING REQUIRED (IE: No mention of our company or logo on the template please)

Target Market(s)

Bars/restaurants

Colors
3176b5
00a990

```html
<!DOCTYPE html>
<html lang="en">
<head>
<meta charset="UTF-8">
<title>The Rules</title>
<link href="https://fonts.googleapis.com/css2?family=Signika:wght@400;600&family=Gentium+Book+Plus:wght@400;700&display=swap" rel="stylesheet">
<style>
  :root {
    --teal: #00a38c;
    --teal-deep: #008f7b;
    --blue: #3176b5;
    --blue-dark: #2a63a0;
    --ink: #1e3f72;
    --body-left: #d3e1ec;
    --body-right: #c9ece6;
    --gold-light: #f6ecc2;
    --gold: #d8bb6a;
    --gold-dark: #b8953f;
  }
  * { margin: 0; padding: 0; box-sizing: border-box; }
  html, body { width: 1200px; height: 675px; overflow: hidden; }
  body { font-family: "Gentium Book Plus", "Palatino Linotype", serif; }
  .slide {
    position: relative;
    width: 1200px;
    height: 675px;
    background: linear-gradient(90deg, var(--body-left) 0%, var(--body-right) 100%);
    overflow: hidden;
  }
  .header-band {
    position: absolute; left: 0; top: 0; width: 100%; height: 149px;
    background: linear-gradient(180deg, var(--teal) 0%, var(--teal-deep) 100%);
  }
  .header-rule {
    position: absolute; left: 0; top: 149px; width: 100%; height: 8px;
    background: var(--blue);
    border-bottom: 1px solid var(--blue-dark);
  }
  .footer-rule {
    position: absolute; left: 0; top: 645px; width: 100%; height: 7px;
    background: var(--blue);
  }
  .footer-band {
    position: absolute; left: 0; top: 652px; width: 100%; height: 23px;
    background: var(--teal);
  }
  .slide-title {
    position: absolute; left: 0; top: 44px; width: 100%;
    text-align: center;
    font-family: "Signika", "Candara", sans-serif;
    font-weight: 600;
    font-size: 64px;
    line-height: 1;
    letter-spacing: 1px;
    color: var(--gold);
    background: linear-gradient(180deg, var(--gold-light) 0%, var(--gold) 55%, var(--gold-dark) 100%);
    -webkit-background-clip: text;
    background-clip: text;
    -webkit-text-fill-color: transparent;
    filter: drop-shadow(3px 4px 3px rgba(0, 40, 40, 0.55));
  }
  .rules-list {
    position: absolute; left: 112px; top: 180px; width: 1010px;
    list-style: none;
    color: var(--ink);
    font-size: 21px;
    line-height: 24px;
  }
  .rules-list li {
    position: relative;
    padding-left: 33px;
    margin-bottom: 5px;
  }
  .rules-list li::before {
    content: "";
    position: absolute; left: 0; top: 8px;
    width: 10px; height: 10px;
    border: 1.5px solid var(--ink);
  }
  .rules-list li::after {
    content: "";
    position: absolute; left: 3px; top: 11px;
    width: 4px; height: 4px;
    background: var(--ink);
  }
  .rules-list strong { font-weight: 700; }
</style>
</head>
<body>
  <main class="slide">
    <div class="header-band"></div>
    <div class="header-rule"></div>
    <h1 class="slide-title">The Rules</h1>
    <ul class="rules-list">
      <li>Teams may have a maximum of <strong>6</strong> players.</li>
      <li>No outside help (internet, phone, etc.) of any kind, including during breaks!&nbsp; If you are<br>caught, your team will be disqualified.</li>
      <li>The game is comprised of 7 rounds of 10 questions&thinsp;—&thinsp;each round is worth 20 points<br>unless otherwise noted.&nbsp; At the end of each round, teams will exchange answer sheets to<br>be graded.&nbsp; After 7 rounds, there will be a FINAL TRIVIA round where each team may<br>wager up to 20 points on a single question.</li>
      <li>Before the game begins, each team must pick one BONUS category (excluding the Final<br>Trivia round) for which they will be awarded double points.</li>
      <li>In the event of a tie, a tie-breaker question will decide the winner.&nbsp; In the unlikely event<br>that the tied teams each answer the question correctly (closest), the winner shall be the<br>team which hands the correct answer to the Quizmaster the quickest.</li>
      <li>The winning team (defined as 2 or more members on the same team, or 1 member if the<br>winner was an individual) from the previous week shall be assessed a handicap equal to<br>½ of their winning margin (rounded down).</li>
      <li>The Quizmaster has final say on all rule interpretations and disputes.</li>
    </ul>
    <div class="footer-rule"></div>
    <div class="footer-band"></div>
  </main>
</body>
</html>
```